Property management company looking for modern card design

We at Blue Maple Holdings provides property management services for its residential and commercial properties, with expertise in all categories of multifamily, industrial and office projects throughout California.

We need a business card design that is professional and modern designed business card. In our field, clients get hundreds of business cards, we would like our card to stand out.

Please avoid small print.

Target Market(s)

Professionals and high end clients

Industry/Entity Type

Financial Planning

Contact Information for Business Card

Company Name: Blue Maple Holdings, Name, email, license #, phone number, website bluemapleholdings.example

Font styles to use
Sans Serif

Requirements
Must have
• The card design needs to be adaptable because there is a possibly we will be expanding into different sectors other than real estate. The card design should be focused on financial planning and asset management.
Nice to have
• Modern and simple business card. Eye catching. Non-standard size/shaped cards would be great.
• bluemapleholdings.example
Should not have
• Too many bright color or any pictures or shapes of real estate stuff.

```html
<!DOCTYPE html>
<html lang="en">
<head>
<meta charset="utf-8">
<title>Blue Maple Holdings – Business Card</title>
<link rel="stylesheet" href="https://fonts.googleapis.com/css2?family=Raleway:wght@400&family=Lora:wght@400;500&family=Open+Sans:wght@400&display=swap">
<style>
  :root {
    --bg: #e4e4e2;
    --paper: #fdfdfc;
    --ink: #1c1c1c;
    --black-card: #1e1e1f;
    --red: #e0141b;
    --faint: #f6ddd2;
    --grey-text: #333;
    --edge: #c50f14;
  }
  * { margin: 0; padding: 0; box-sizing: border-box; }
  html, body { width: 1200px; height: 1021px; overflow: hidden; background: var(--bg); }
  .canvas { position: relative; width: 1200px; height: 1021px; }

  .card {
    position: absolute;
    width: 560px;
    height: 320px;
    border-bottom: 8px solid var(--edge);
    box-shadow: 0 10px 24px rgba(0,0,0,.18);
    overflow: hidden;
  }
  .card-front { left: 70px; top: 110px; background: var(--paper); }
  .card-back  { left: 570px; top: 580px; background: var(--black-card); }

  .faint-circle {
    position: absolute;
    right: 40px; top: 14px;
    width: 230px; height: 230px;
    border-radius: 50%;
    background: var(--faint);
    opacity: .7;
  }

  .wordmark {
    position: absolute;
    font-family: "Raleway", sans-serif;
    font-weight: 400;
    letter-spacing: 1px;
    line-height: 1;
    text-transform: uppercase;
  }
  .card-front .wordmark { right: 32px; top: 110px; font-size: 30px; color: var(--ink); text-align: right; }
  .card-back .wordmark { left: 200px; top: 132px; font-size: 30px; color: #fff; }
  .wordmark small { display: block; font-size: 14px; letter-spacing: 7px; margin-top: 8px; }

  .logo-dot {
    position: absolute;
    left: 100px; top: 112px;
    width: 80px; height: 80px;
    border-radius: 50%;
    background: var(--red);
  }

  .person {
    position: absolute;
    left: 36px; top: 128px;
    padding-left: 16px;
    border-left: 6px solid var(--red);
    font-family: "Lora", serif;
  }
  .person-name { font-size: 24px; font-weight: 500; color: var(--ink); line-height: 1.05; }
  .person-title { font-size: 15px; color: var(--red); }

  .contacts {
    position: absolute;
    left: 40px; bottom: 28px;
    list-style: none;
    font-family: "Open Sans", sans-serif;
    font-size: 14px;
    color: var(--grey-text);
  }
  .contacts li { display: flex; align-items: center; gap: 10px; margin-top: 4px; }
  .contacts svg { width: 13px; height: 13px; fill: var(--red); flex: none; }
</style>
</head>
<body>
<main class="canvas">

  <section class="card card-front" aria-label="Card front">
    <div class="faint-circle" aria-hidden="true"></div>
    <div class="wordmark">Blue Maple<small>Holdings</small></div>

    <div class="person">
      <p class="person-name">Your Name</p>
      <p class="person-title">Job Title</p>
    </div>

    <ul class="contacts">
      <li>
        <svg viewBox="0 0 16 16" aria-hidden="true"><path d="M3 2l3 0 1 4-2 1a9 9 0 0 0 4 4l1-2 4 1 0 3c0 1-1 2-2 2A12 12 0 0 1 1 4c0-1 1-2 2-2z"/></svg>
        000 000 0000
      </li>
      <li>
        <svg viewBox="0 0 16 16" aria-hidden="true"><path d="M1 3h14v10H1z M2 4l6 5 6-5" fill="none" stroke="#e0141b" stroke-width="1.6"/></svg>
        youremail@xyz.com
      </li>
      <li>
        <svg viewBox="0 0 16 16" aria-hidden="true"><g fill="none" stroke="#e0141b" stroke-width="1.4"><circle cx="8" cy="8" r="6.5"/><ellipse cx="8" cy="8" rx="3" ry="6.5"/><path d="M1.5 8h13"/></g></svg>
        www.bluemapleholdings.example
      </li>
    </ul>
  </section>

  <section class="card card-back" aria-label="Card back">
    <div class="logo-dot" aria-hidden="true"></div>
    <div class="wordmark">Blue Maple<small>Holdings</small></div>
  </section>

</main>
</body>
</html>
```